Solar Advertising Flier to generate Biz

I need a advertisement that generates business to be used in a mailer for marketing purposes.

Im attaching a file that is a an idea of advertisement.
I do not want the "ZVN" specific information on it.
I want the background solar panels.
Same information as the ad.
And I've attached my Logo - I want the color scheme to match this.

Thank you

Target Market(s)

Middle to Upper Class Home Owners

Industry/Entity Type

Solar Energy

Requirements
Must have
• A call to action
• A professional look
Nice to have
• A family
• Great looking solar panels
Should not have
• Cartoons

```html
<!DOCTYPE html>
<html lang="en">
<head>
<meta charset="utf-8">
<title>Go Solar – Brightfield Power Flier</title>
<link href="https://fonts.googleapis.com/css2?family=Bebas+Neue&family=Open+Sans:wght@400;600;700&display=swap" rel="stylesheet">
<style>
  :root {
    --white: #ffffff;
    --promo-green: #41ae49;
    --brand-blue: #00aeef;
    --brand-green: #8cc63f;
    --brand-ink: #1a9bd7;
    --sky-top: #b9dcf3;
    --sky-mid: #8fb7de;
    --roof-red: #d8643a;
    --brick: #7a4a35;
    --panel-dark: #2c3b52;
  }
  html, body {
    margin: 0;
    padding: 0;
    width: 922px;
    height: 1200px;
    overflow: hidden;
    background: var(--white);
  }
  .flier {
    position: relative;
    width: 922px;
    height: 1200px;
    background: var(--white);
    font-family: "Open Sans", Arial, sans-serif;
    color: var(--white);
  }
  .family-photo {
    position: absolute;
    left: 18px; top: 21px;
    width: 444px; height: 346px;
    background: linear-gradient(180deg, var(--sky-top) 0%, #cfe3f2 35%, var(--roof-red) 55%, #c98a5e 75%, #6c7a84 100%);
  }
  .roof-photo {
    position: absolute;
    left: 485px; top: 21px;
    width: 412px; height: 628px;
    background: linear-gradient(160deg, #5d7fae 0%, var(--sky-mid) 25%, #c9d3dd 40%, var(--panel-dark) 55%, #3e4d66 70%, var(--brick) 85%, #5a3527 100%);
  }
  .brand-tag {
    position: absolute;
    left: 532px; top: 21px;
    width: 116px; height: 108px;
    background: var(--white);
    display: flex;
    flex-direction: column;
    align-items: center;
    justify-content: center;
    gap: 8px;
  }
  .brand-tag__dot {
    width: 30px; height: 30px;
    border-radius: 50%;
    background: var(--brand-green);
  }
  .brand-tag__name {
    font-size: 12px;
    font-weight: 600;
    color: var(--brand-ink);
    text-align: center;
    line-height: 1.2;
  }
  .rebate {
    position: absolute;
    left: 18px; top: 402px;
    width: 444px; height: 247px;
    background: var(--promo-green);
    text-align: center;
    overflow: hidden;
  }
  .rebate__lead {
    position: absolute; left: 0; right: 0; top: 13px;
    font-size: 28px; font-weight: 600; line-height: 38px;
  }
  .rebate__amount {
    position: absolute; left: 0; right: 0; top: 63px;
    font-size: 104px; font-weight: 600; line-height: 1;
    letter-spacing: -1px;
  }
  .rebate__label {
    position: absolute; left: 0; right: 0; top: 161px;
    font-size: 29px; font-weight: 700; letter-spacing: 4px; line-height: 40px;
  }
  .rebate__terms {
    position: absolute; left: 16px; right: 16px; top: 207px;
    margin: 0;
    font-size: 11px; line-height: 13px;
  }
  .offer-band {
    position: absolute;
    left: 0; top: 671px;
    width: 922px; height: 529px;
    background: var(--brand-blue);
  }
  .headline {
    position: absolute;
    left: 40px; width: 356px; top: 50px;
    margin: 0;
    font-family: "Bebas Neue", Impact, sans-serif;
    font-weight: 400;
    font-size: 164px;
    line-height: 146px;
    text-align: center;
  }
  .grandfather {
    position: absolute;
    left: 20px; width: 396px; top: 358px;
    margin: 0;
    font-size: 29px; font-weight: 600;
    line-height: 44px;
    text-align: center;
  }
  .benefits {
    position: absolute;
    left: 435px; top: 41px; width: 447px;
    margin: 0; padding: 0;
    list-style: none;
  }
  .benefits li {
    position: relative;
    padding-left: 17px;
    font-size: 24.5px; font-weight: 600;
    line-height: 25px;
    margin-bottom: 14px;
  }
  .benefits li::before {
    content: "";
    position: absolute;
    left: 0; top: 5px;
    width: 2px; height: 16px;
    background: var(--white);
  }
  .divider {
    position: absolute;
    left: 441px; top: 300px;
    width: 425px; height: 3px;
    background: var(--white);
  }
  .contact {
    position: absolute;
    left: 410px; width: 490px; top: 328px; height: 180px;
    text-align: center;
  }
  .contact p { position: absolute; left: 0; right: 0; margin: 0; }
  .contact__prompt { top: 0; font-size: 19.5px; font-weight: 600; line-height: 24px; }
  .contact__phone { top: 38px; font-size: 55px; font-weight: 700; line-height: 66px; }
  .contact__address { top: 108px; font-size: 25px; font-weight: 600; line-height: 32px; }
  .contact__web { top: 144px; font-size: 21px; font-weight: 600; line-height: 28px; }
</style>
</head>
<body>
<div class="flier">
  <div class="family-photo" role="img" aria-label="Smiling family of three standing in front of a new house with solar panels on its red tile roof"></div>
  <div class="roof-photo" role="img" aria-label="Brick house roof covered with dark solar panels under a blue cloudy sky"></div>
  <div class="brand-tag">
    <span class="brand-tag__dot"></span>
    <span class="brand-tag__name">Brightfield Power</span>
  </div>

  <section class="rebate">
    <div class="rebate__lead">Call today and receive a</div>
    <div class="rebate__amount">$500</div>
    <div class="rebate__label">CASH REBATE</div>
    <p class="rebate__terms">Limited time offer. Ad must be present at time of purchase. Call for<br>details. Not valid with any other offer or on previous purchases.</p>
  </section>

  <section class="offer-band">
    <h1 class="headline">GO<br>SOLAR</h1>
    <p class="grandfather">Get grandfathered<br>before the new<br>deadline</p>
    <ul class="benefits">
      <li>$0 down, no upfront cost</li>
      <li>Save upto 90% off your utility bill</li>
      <li>Protect against inflation &amp; energy<br>costs increases from your Utility<br>Company</li>
      <li>Provide clean, reliable energy for<br>your family powered by sun</li>
    </ul>
    <div class="divider"></div>
    <div class="contact">
      <p class="contact__prompt">Call today for a no obligation consultation</p>
      <p class="contact__phone">555-014-2276</p>
      <p class="contact__address">4150 W Juniper Rd AZ 85000</p>
      <p class="contact__web">www.BrightfieldSolar.com</p>
    </div>
  </section>
</div>
</body>
</html>
```